Mobile Marketing Business needs a UNIQUE web design that makes users stop, adore and engage!

Unique web design for a new division of our company. Based in Los Angeles, TornaCell is a mobile marketing company offering mobile optimized websites, sms marketing, strategic and analytic consultation services. We are a b2b model targeting a wide range of industries and business sizes. Our parent company is Harbrook Digital. Tornacell needs to reflect a progressive nature, confidence, and experience - yet affordable to any business that wants to reach the mobile consumer. We want to avoid a dark website or one that is too bland. The colors should be strong, yet not overly so.

Layout should be clean, focused, - avoiding a cluttered home page. Visitors should recognize WE ARE mobile marketing - it should resonate that WE differ from competitors - Site design should resonate our brand! We've noticed competitors sites start to look and feel like the same - where the visitor may quickly exit from the home page or first inner page. There are some sites that differ which we've listed below.

The audience will range from sophisticated marketers to a local business operator who is not web savvy. The site should welcome all - not intimidate some while wowing others. We understand it's difficult for websites to be a "one size fits all" - but in reviewing competitive sites, it's apparent no one site really leaves any key impression. We'd like Tornacell to be the one.

The site should invite user to engage with the site and compel them to contact us for a demo for a better understanding of how mobiele marketing is the ultimate one 2 one sales channel that can help them improve gross sales.

Site should not be "dark" which requires using white font - we do not want "wild" or "fluorescent" colors. A tasteful, classic balance of colors that provides a comfortable experience to engage.

We realize this challenge seems .. well extremely challenging but we're quite confident there is a "design ninja" lurking out there. Are YOU the one?

Happy to provide more details and info as needed.

Sample sites that we like and feel are unique to the industry and also a site that we feel is quite basic:

www.pelvarstudio.com - clever use of banner area and using a slider to present services. However, labeling the sliders as such is a little difficult to read.

www.brantiqo.ca - clean, classic, minimalistic. Perhaps too minimal for our need but we like it. Nice use of the varying sizes and treatment of 3 promo boxes under main banner. Inner page layout is nice.

www.quarvelo.com - clever, unique. Love the call to action box (adjacent to phone) offering 3 options for next steps. Inner pages are well designed - overall site is clean, easy to read and merchandises offerings effectively.

www.brightmarshgroup.com - clean, well merchandised but home page is a bit too cluttered. good use of colors, inner page layout is simple but effective.

www.delvapost.com - clean, simple easy to follow.

www.trimesk.com - pretty basic site - in fact, you could probably replace the logo with another marketing company, etc. and the site would most likely work. We would prefer to avoid this stigma for TornaCell!!

NOTE: our logo uses a bright green that may limit it's use for mostly accents, etc. We like the contrast of colors used on www.zelnavor.com and www.paddockreel.com.au/ using the dark gray background and other colors to bring some life.

If you google "mobile marketing company", "mobile marketing services", "text messaging services", etc.. you'll notice 2 distinctive categories: amazing - like what the heck were they thinking.. and yawn - like here's another one that looks like the other..
Updates

Thank you everyone for the submissions - while they are nice, I have to say they fall into the category we were hoping to avoid (yawn, this one looks like all the other company sites)..  

Please do review the brief thoroughly - we're available if you need a specific issue addressed.  

We're still hoping a design ninja surfaces and provides a comp that makes us go "WOW'..  

cheers and good luck!

Thanks for your participation -  please stay tuned for an update to the brief along with some copy to populate the home page.  

Also... keep an eye on the project award..  we'll be increasing it after posting updates!

cheers.

UPDATE!  We have INCREASED the award in hopes of inspiring you great designers to entice your imagination and creative genetics!

PLEASE feel free to ask for further clarification or even if you want to run something by before submitting a design.  

We also have several other projects and would certainly consider those designers that truly impressed us.

As promised we're adding a bit more detail to this project.  The project requires a home and inner page layout but would like to start with the home page first.   We would also like to have a blog that differs a bit but retain some core elements of the site design.

This is a new design - our desire is to launch a website bearing an effective yet distinctive look.  Again, if you google "mobile marketing services", "mobile marketing company/companies", "mobile ..." aside from the logo varying most of the sites look the same.    We want something different..

The following may be repetitive from our brief but here goes:

Banner will focus on 3 categories - SMS/Text Marketing, Mobile Websites and Mobile Marketing:  
#1)  Headline - Did you notice how many consumers are on smartphones today?  Reach them now. 
Sub text - Mobile coupons get 10 times the redemption rate of traditional coupons
Text messages are read by 94% of recipients within 4 minutes
50% of SMS users are aged 35+ 

#2) Headline - Every day 53% of Americans use their smartphone to search the web.  Do you have a mobile optimized website?   You could be missing all these consumers each day. 
Sub text - 95% of smarthphone users search for local information 
                         70% of all mobile searches result in action within 1 hour
#3) Headline - Break through the clutter - innovative marketing campaigns distinguish your brand
Sub text - Integrate social and mobile campaigns whenever and wherever
 91% of U.S. population have a mobile device within reach 24/7

** We are open to suggestions for images or style of banner - 

Below the banner would like to have a content section featuring rotating messages titled as:
  
DID YOU KNOW? }   There are 5 times as many texters as there are Chatterly users?   < note 3-4 messages will scroll - a read more text link to an inner page for more of these facts.. 

Need 3 content sections - would prefer atypical format - not boxes, or framed areas but something different - titled:
What is a mobile website?  
Connect with mobile consumers
Mobile marketing revolution

Need:  
** a login icon for clients to access; contact us, email and text message optin - (see reference to Wendrop and Quarvelo sites from prior brief - wendrop uses creative fonts for the contact us box and email /sms optin,  quarvelo uses a creative call to action adjacent to the mobile phone with 3 options)

** to see active/ mouse over effect for navigation
** avoid a really long page - perhaps using scripts to reveal drop down boxes in content sections if necessary. 
** use of complimentary colors - keeping to white with elements of just black and green from logo gets boring
**  interesting yet not distracting shapes
** need to avoid bubble gum or flouorescent colors - note wendrop mixes colors in the main banner area in an interesting fashion. 

** need frameless design  

Again, reference the sites we liked .. and didn't like on the original brief.  Additionally we also like these sites:

1) kelbrix.com - open, expansive area - uncluttered,

2) http://presskit.daltonherald.com - love the layout and use of the black to emulate ink against white paper tying into the newspaper / brand.  We LOVE LOVE LOVE.. that sort of creativity.. in fact this is perhaps one of our favorite sites and how efficient and unique content sections, buttons, navigation, etc. is 

Looking forward to your submissions - cheers!!   

Reason: Attention all designers - this is the final extension! There are some great comps rolling in so PLEASE get your designs in soon !!!

Target Market(s)

Quite diverse actually - from local businesses (e.g., trades, professional services, retail, restaurant, hospitality, etc.) to agencies.

Industry/Entity Type

Progressive

Requirements
Must have
• Main banner of sort for messaging - would like to present 4-5 key messages that rotate/ fade on topics of SMS, mobile users, etc.
We were wondering if using mobile devices as pelvarstudio.com did to feature messages - but perhaps this limits amount of text. Also like the www.wendrop.com site with the banner rotating but also revealing portions of the slide before and after.

3-4 sections to promote key content that link to inner pages. These will feature some text - e.g., see www.brantiqo.ca - creative use of staggering box height and using script to reveal.

Main navigation = Home, Why Mobile, What We Do, Services, News (a blog), Contact. There will be 3-8 subpages for Why mobile, what we do, and services.

Footer - should contain email / text messaging sign up - see www.wendrop.com for their optin in design.

Get in Touch- again, love how www.wendrop.com has designed the "Get in Touch" call to action - not the typical button shape.

Blog - absolutely

Social icons - chatterly , workvine, and..?
Nice to have
• Not sure what we'd need here - unless you have an idea. We're open to suggestions despite our strong opinions stated so far..
Should not have
• Avoid:
anything too extreme -
avoid cartoon type illustrations
heavy use of icons
extreme colors
font that is hard to read..

```html
<!DOCTYPE html>
<html lang="en">
<head>
<meta charset="utf-8">
<title>TornaCell — Mobile Marketing Company</title>
<link href="https://fonts.googleapis.com/css2?family=PT+Sans:wght@400;700&family=Ubuntu:wght@400&display=swap" rel="stylesheet">
<style>
:root{
  --green:#a9dc36;
  --green-text:#8cbf26;
  --header:#1b1b1b;
  --hero:#2b2b2b;
  --panel:#222;
  --ink:#222;
  --muted:#555;
  --footer:#ebebeb;
  --white:#fff;
  --orange:#f29a0c;
}
*{box-sizing:border-box;margin:0;padding:0}
html,body{width:1096px;height:1200px;overflow:hidden}
body{font-family:"PT Sans",sans-serif;color:var(--ink);background:var(--white);position:relative}
.abs{position:absolute}

.site-header{left:0;top:0;width:1096px;height:84px;background:var(--header);border-bottom:1px solid #333}
.brand{left:137px;top:22px;color:var(--white)}
.brand-name{display:flex;align-items:center;gap:6px;font-size:28px;line-height:1;color:var(--green)}
.brand-name .mark{width:14px;height:14px;background:var(--green)}
.brand-tag{font-size:10px;letter-spacing:1.5px;color:#aaa;margin-top:4px;padding-left:3px}
.main-nav a{position:absolute;top:30px;height:26px;line-height:26px;font-size:10px;font-weight:700;color:#ddd;text-decoration:none;letter-spacing:.3px}
.main-nav a.active{background:var(--green);color:var(--white);border-radius:4px;width:66px;text-align:center}

.hero{left:0;top:84px;width:1096px;height:453px;background:linear-gradient(#2e2e2e,#252525)}
.hero-title{left:137px;top:50px;color:var(--white);font-size:40px;line-height:42px;font-weight:400;letter-spacing:-.5px}
.hero-text{left:137px;top:141px;width:370px;color:var(--white);font-size:11px;line-height:14px}
.promo{left:138px;top:226px;width:246px;height:106px}
.promo-body{left:38px;top:16px;width:160px;color:var(--white)}
.promo-num{left:13px;top:15px;width:14px;height:14px;border-radius:50%;background:var(--green);color:var(--white);font-size:8px;text-align:center;line-height:14px}
.promo-body h3{font-weight:400;font-size:16px;margin-top:-4px}
.promo-body p{font-size:9px;line-height:12px;color:#999;margin-top:5px;padding-left:1px}
.promo-link{left:150px;top:88px;color:var(--white);font-size:11px}
.dots{left:312px;top:373px;display:flex;gap:9px}
.dots span{width:8px;height:8px;border-radius:50%;background:#111}
.dots span.on{background:var(--green)}
.device-art{left:583px;top:34px;width:378px;height:405px;border-radius:30px;background:linear-gradient(135deg,#3a3a3a,#0c0c0c 60%,#1e1e1e)}
.try-badge{left:571px;top:341px;width:68px;height:68px;border-radius:50%;background:radial-gradient(circle at 45% 40%,#ffb21d,var(--orange));color:var(--white);font-size:12px;display:flex;align-items:center;justify-content:center}

.tagline{left:0;top:565px;width:1096px;text-align:center;font-family:"Ubuntu",sans-serif;font-size:25px;line-height:31px;color:var(--ink)}
.tagline em{font-style:normal;color:var(--green-text)}
.divider{left:137px;top:663px;width:826px;height:7px;background:#e2e2e2}

.section-title{font-size:17px;font-weight:400;color:var(--ink)}
.clients{left:137px;top:706px;width:480px}
.clients p{font-size:11px;line-height:14px;margin-top:6px}
.client-logos{left:137px;top:790px;display:flex;align-items:center;gap:34px}
.client{display:flex;align-items:center;gap:6px;font-size:22px;color:#555}
.client .dot{width:14px;height:14px;border-radius:50%;background:#666}
.pill{left:137px;top:871px;width:94px;height:16px;border-radius:8px;background:var(--green);color:var(--white);font-size:9px;text-align:center;line-height:16px}

.touch{left:647px;top:706px;width:316px}
.touch p{font-size:11px;margin-top:8px}
.touch p em{font-style:normal;color:var(--green-text)}
.newsletter{left:646px;top:758px;width:317px;height:125px;background:var(--panel)}
.newsletter-bar{height:40px;background:var(--green);padding:8px 10px;display:flex;gap:9px}
.newsletter-bar .field{flex:1;background:var(--white);font-size:9px;color:#aaa;padding:7px 8px}
.newsletter-bar .btn{width:76px;background:var(--header);color:var(--white);font-size:11px;text-align:center;line-height:24px}
.newsletter-copy{padding:12px 11px 0;color:var(--white);font-size:9px;line-height:12px}
.newsletter-link{padding:11px 13px;color:var(--green);font-size:9px}

.site-footer{left:0;top:958px;width:1096px;height:242px;background:var(--footer)}
.f-col{top:50px}
.f-col h4{font-weight:400;font-size:17px;color:var(--ink)}
.f-list{list-style:none;margin-top:16px}
.f-list li{font-size:10px;color:var(--muted);height:25.3px;padding-left:12px;position:relative}
.f-list li::before{content:"";position:absolute;left:0;top:3px;border-left:5px solid #333;border-top:3.5px solid transparent;border-bottom:3.5px solid transparent}
.f-list li.hl{color:var(--green-text)}
.social{display:flex;gap:9px;margin-top:31px}
.social span{width:27px;height:27px;border-radius:50%;background:#555}
.social span.on{background:var(--green)}
.signup .input{width:243px;height:28px;border:1px solid #ccc;background:#f4f4f4;font-size:10px;color:#333;padding:7px 12px;margin-top:6px}
.signup .input:first-of-type{margin-top:16px}
.signup .btn{width:61px;height:21px;background:var(--green);border-radius:3px;color:var(--white);font-size:10px;text-align:center;line-height:21px;margin-top:8px}
.rule{left:137px;top:199px;width:826px;height:1px;background:#ccc}
.copyright{left:0;top:213px;width:1096px;text-align:center;font-size:10px;color:#444}
</style>
</head>
<body>

<header class="site-header abs">
  <div class="brand abs">
    <div class="brand-name"><span class="mark"></span>TornaCell</div>
    <div class="brand-tag">Mobile Marketing Company</div>
  </div>
  <nav class="main-nav">
    <a class="active" style="left:386px">HOME</a>
    <a style="left:482px">WHY MOBILE</a>
    <a style="left:590px">WHAT WE DO</a>
    <a style="left:706px">SERVICES</a>
    <a style="left:806px">NEWS</a>
    <a style="left:895px">CONTACT</a>
  </nav>
</header>

<section class="hero abs">
  <h1 class="hero-title abs">SMS<br>Short Message Service</h1>
  <p class="hero-text abs">Short Message Service (SMS) is a text messaging service component of phone, web, or mobile communication systems, using standardized communications protocols that allow the exchange of short text messages between fixed line or mobile phone devices.</p>

  <div class="promo abs">
    <svg class="abs" width="246" height="106" viewBox="0 0 246 106">
      <polygon points="0,0 226,0 196,58 0,85" fill="#1c1c1c"/>
      <polygon points="226,22 246,22 216,56 246,106 226,106 196,58" fill="#a9dc36"/>
      <rect x="21" y="85" width="205" height="21" fill="#a9dc36"/>
    </svg>
    <span class="promo-num abs">1</span>
    <div class="promo-body abs">
      <h3>Emergency Services</h3>
      <p>In some countries SMS messages can be used to contact the emergency services.</p>
    </div>
    <span class="promo-link abs">Readmore ›</span>
  </div>

  <div class="dots abs"><span class="on"></span><span></span><span></span><span></span></div>

  <div class="device-art abs" role="img" aria-label="Two smartphones showing the TornaCell text messaging app"></div>
  <div class="try-badge abs">Try it</div>
</section>

<h2 class="tagline abs">TornaCell is the leading mobile marketing<br>company in <em>Los Angeles</em></h2>
<div class="divider abs"></div>

<section class="clients abs">
  <h3 class="section-title">Who we work with</h3>
  <p>Lorem ipsum dolor sit amet, consectetuer adipiscing elit, sed diam nonummy nibh euismod tincidunt ut.</p>
</section>
<div class="client-logos abs">
  <div class="client">Robotix</div>
  <div class="client"><span class="dot"></span>Panelsoft Mobile</div>
  <div class="client">Orchard</div>
</div>
<div class="pill abs">View more client</div>

<section class="touch abs">
  <h3 class="section-title">Get in touch</h3>
  <p>Receive Our <em>Monthly Newsletter</em></p>
</section>
<div class="newsletter abs">
  <div class="newsletter-bar">
    <div class="field">Your email here...</div>
    <div class="btn">Submit</div>
  </div>
  <p class="newsletter-copy">Ut wisi enim ad minim veniam, quis nostrud exerci tation ullamcorper suscipit lobortis nisl ut aliquip ex ea commodo consequat.</p>
  <p class="newsletter-link">About Newsletter</p>
</div>

<footer class="site-footer abs">
  <div class="f-col abs" style="left:137px">
    <h4>What we do ?</h4>
    <ul class="f-list">
      <li>Lorem ipsum dolor sit amet</li>
      <li>Consectetuer adipiscing elit</li>
      <li class="hl">Sed diam nonummy nibh</li>
      <li>Euismod tincidunt ut.</li>
    </ul>
  </div>
  <div class="f-col abs" style="left:330px">
    <h4>Links</h4>
    <ul class="f-list">
      <li class="hl">Lorem ipsum dolor sit amet</li>
      <li>Consectetuer adipiscing elit</li>
      <li>Sed diam nonummy nibh</li>
      <li>Euismod tincidunt ut.</li>
    </ul>
  </div>
  <div class="f-col abs" style="left:524px">
    <h4>Follow</h4>
    <div class="social"><span class="on"></span><span></span><span></span><span></span></div>
  </div>
  <div class="f-col signup abs" style="left:720px">
    <h4>Sign Up</h4>
    <div class="input">Name</div>
    <div class="input">Email</div>
    <div class="btn">Submit</div>
  </div>
  <div class="rule abs"></div>
  <p class="copyright abs">Copyright © 2012 TornaCell. All right reserved</p>
</footer>

</body>
</html>
```